Southport Billboard for Hiring more CDL drivers

I need a catch design for a bill board (size 10ft by 36 ft) to catch the attention for semi truck drivers.
In the design I want it to include:
-My company logo along with my website(ridgewaycarriers.com) and my number(803-555-0172) for contact info.
-I also need it to say earn up to $90,000 a year
-I will send a few photos to choose from
-I need the logo to look clean and simple! I don't want it to be cluttered just clean, simple and catchy.!

Target Market(s)

CDL Class A holders
Semi Truck Drivers

Industry/Entity Type

Trucking Company

Font styles to use
Other font styles liked:
• a font to match my logo

Requirements
Must have
• "Make up to $90,000"
"ridgewaycarriers.com"
"803-555-0172"

```html
<!DOCTYPE html>
<html lang="en">
<head>
<meta charset="utf-8">
<title>Ridgeway Carriers – CDL Driver Billboard</title>
<link rel="stylesheet" href="https://fonts.googleapis.com/css2?family=Anton&family=Archivo+Black&family=Roboto+Condensed:wght@800&display=swap">
<style>
  :root {
    --ink-dark: #1f2420;
    --brand-red: #e31b23;
    --paper: #ffffff;
    --backdrop: #d9d9d9;
    --truck-mint: #a9c2b4;
    --truck-shadow: #3a443e;
  }
  * { margin: 0; padding: 0; box-sizing: border-box; }
  html, body {
    width: 1200px;
    height: 1200px;
    overflow: hidden;
    background: var(--backdrop);
  }
  .billboard {
    position: absolute;
    left: 60px;
    top: 450px;
    width: 1080px;
    height: 300px;
    background: var(--ink-dark);
    box-shadow: 0 14px 30px rgba(0,0,0,0.35);
    overflow: hidden;
  }
  .billboard-shapes {
    position: absolute;
    inset: 0;
    width: 1080px;
    height: 300px;
  }
  .brand-name {
    position: absolute;
    left: 34px;
    top: 46px;
    width: 240px;
    font-family: "Anton", sans-serif;
    color: var(--ink-dark);
    font-size: 60px;
    line-height: 1.05;
    letter-spacing: 1px;
    text-transform: uppercase;
  }
  .truck-photo {
    position: absolute;
    left: 402px;
    top: 10px;
    width: 340px;
    height: 222px;
    border-radius: 40% 45% 16% 16% / 50% 50% 14% 14%;
    background: radial-gradient(ellipse at 60% 50%, var(--truck-mint) 0%, #7f978a 45%, var(--truck-shadow) 78%, rgba(31,36,32,0) 100%);
  }
  .headline {
    position: absolute;
    left: 776px;
    top: 0;
    width: 300px;
    height: 240px;
    font-family: "Anton", sans-serif;
    font-weight: 400;
    text-transform: uppercase;
    color: var(--paper);
  }
  .headline span {
    position: absolute;
    left: 0;
    width: 100%;
    text-align: center;
    white-space: nowrap;
  }
  .headline-lead {
    top: 22px;
    font-size: 44px;
    line-height: 44px;
    letter-spacing: 3px;
  }
  .headline-amount {
    top: 76px;
    font-size: 86px;
    line-height: 86px;
    color: var(--brand-red);
  }
  .headline-tail {
    top: 178px;
    font-size: 44px;
    line-height: 44px;
    letter-spacing: 3px;
  }
  .contact {
    position: absolute;
    top: 240px;
    height: 60px;
    display: flex;
    align-items: center;
    color: var(--paper);
    white-space: nowrap;
  }
  .contact-phone { left: 29px; }
  .contact-web { left: 535px; }
  .contact-icon { width: 38px; height: 38px; margin-right: 13px; flex: none; }
  .phone-number {
    font-family: "Archivo Black", sans-serif;
    font-size: 46px;
    letter-spacing: 2px;
    line-height: 1;
  }
  .web-address {
    font-family: "Roboto Condensed", sans-serif;
    font-weight: 800;
    font-size: 48px;
    line-height: 1;
  }
</style>
</head>
<body>
  <section class="billboard" aria-label="Ridgeway Carriers driver recruitment billboard">
    <svg class="billboard-shapes" viewBox="0 0 1080 300" aria-hidden="true">
      <path class="logo-panel" fill="var(--paper)" d="M0 0 H337 C330 120 290 200 230 240 H0 Z"/>
      <path class="accent-swoosh" fill="var(--brand-red)" d="M337 0 H373 C365 130 320 205 262 240 H236 C296 200 333 120 339 0 Z"/>
      <path class="accent-swoosh-edge" fill="none" stroke="var(--paper)" stroke-width="3" d="M375 0 C367 130 322 205 264 240"/>
      <rect class="contact-band" x="0" y="240" width="1080" height="60" fill="var(--brand-red)"/>
      <path class="band-divider" fill="var(--ink-dark)" d="M500 240 H528 L500 300 H472 Z"/>
    </svg>

    <div class="brand-name">Ridgeway<br>Carriers</div>

    <div class="truck-photo" role="img" aria-label="Photo of a mint-green semi truck with chrome grille pulling a lowboy trailer"></div>

    <h1 class="headline">
      <span class="headline-lead">Earn up to</span>
      <span class="headline-amount">$90,000</span>
      <span class="headline-tail">A year</span>
    </h1>

    <div class="contact contact-phone">
      <svg class="contact-icon" viewBox="0 0 36 36" aria-hidden="true">
        <circle cx="18" cy="18" r="16" fill="none" stroke="var(--ink-dark)" stroke-width="2.5"/>
        <path fill="var(--ink-dark)" d="M12.5 9.5 l3 -0.5 l2 5 l-2.2 1.6 c0.9 2.3 2.4 4 4.5 5.2 l1.8 -2 l4.8 2.3 l-0.6 3 c-0.3 1 -1.3 1.6 -2.4 1.4 c-6.2 -1.3 -10.6 -6.3 -11.7 -12.5 c-0.2 -1.2 0.3 -2.2 0.8 -3.5 z"/>
      </svg>
      <span class="phone-number">803-555-0172</span>
    </div>

    <div class="contact contact-web">
      <svg class="contact-icon" viewBox="0 0 36 36" aria-hidden="true">
        <circle cx="18" cy="18" r="16" fill="none" stroke="var(--ink-dark)" stroke-width="2.5"/>
        <g fill="none" stroke="var(--ink-dark)" stroke-width="1.6">
          <circle cx="18" cy="18" r="10"/>
          <ellipse cx="18" cy="18" rx="4.5" ry="10"/>
          <line x1="8" y1="18" x2="28" y2="18"/>
          <line x1="9.5" y1="13" x2="26.5" y2="13"/>
          <line x1="9.5" y1="23" x2="26.5" y2="23"/>
        </g>
      </svg>
      <span class="web-address">ridgewaycarriers.com</span>
    </div>
  </section>
</body>
</html>
```